Still Water Healing needs design for Wordpress

I am a Still Water Healing and I need a Wordpress design to offer my distant healing services on a website. It's like Reiki but I use my own healing modality.
It would be great to have a magical design with beautiful colors like purple, I will upload some images so you get an idea of the feel.
The design should communicate lightness and peacefulness, I like playfulness in the design not too blocky.
Need a complete website design, including navigation bar. I do not have a logo yet.

Target Market(s)

Everyone

Requirements
Nice to have
• Works on mobile devices
Should not have
• Too much of typical spiritual symbols on it.

```html
<!DOCTYPE html>
<html lang="en">
<head>
<meta charset="utf-8">
<title>Still Water Healing</title>
<link href="https://fonts.googleapis.com/css2?family=Oswald:wght@300;400&family=Libre+Baskerville:ital@1&family=Open+Sans:ital,wght@0,400;0,600;1,400&display=swap" rel="stylesheet">
<style>
  :root{
    --plum:#45264a;
    --plum-dark:#2e1a30;
    --plum-text:#4a2a4f;
    --header-bg:#ececec;
    --side-bg:#e9e9e9;
    --ink:#222;
    --body:#444;
    --rule:#d6d6d6;
    --footer-text:#e8dfe9;
    --field:#d9d1da;
  }
  *{box-sizing:border-box;margin:0;padding:0}
  html,body{width:900px;height:1200px;overflow:hidden;background:#fff}
  body{position:relative;font-family:"Open Sans",Arial,sans-serif;color:var(--body)}
  .abs{position:absolute}

  /* Header */
  .site-header{left:0;top:0;width:900px;height:82px;background:var(--header-bg)}
  .brand{left:124px;top:30px;font-family:"Oswald",sans-serif;font-weight:400;font-size:20px;color:var(--plum-text);display:flex;align-items:center;gap:8px;letter-spacing:.5px}
  .brand-dot{width:14px;height:14px;border-radius:50%;background:var(--plum-text)}
  .main-nav{right:124px;top:38px;display:flex;gap:28px;font-family:"Oswald",sans-serif;font-weight:400;font-size:12px;color:#333;letter-spacing:.4px}

  /* Hero */
  .hero{left:0;top:82px;width:900px;height:300px;background:linear-gradient(100deg,#3d3a1e 0%,#8a8a48 22%,#5b5a2c 45%,#2f2a14 65%,#6e4a1c 85%,#8a4a1a 100%)}
  .hero-title{left:474px;top:168px;padding:0 12px;height:45px;line-height:45px;background:#fff;font-family:"Oswald",sans-serif;font-size:23px;color:#222;letter-spacing:.6px}
  .hero-text{left:474px;top:226px;width:252px;padding:8px 12px;background:rgba(20,18,14,.75);font-family:"Oswald",sans-serif;font-weight:400;font-size:10px;line-height:17px;color:#fff;letter-spacing:.4px}
  .hero-btn{left:474px;top:300px;width:83px;height:27px;line-height:27px;text-align:center;background:#fff;font-family:"Oswald",sans-serif;font-size:11px;color:#222;letter-spacing:.6px}
  .hero-arrow{top:221px;width:28px;height:28px;border-radius:50%;background:rgba(210,210,210,.8)}
  .hero-arrow svg{display:block}

  /* Intro */
  .intro-title{left:0;top:402px;width:900px;text-align:center;font-family:"Libre Baskerville",Georgia,serif;font-style:italic;font-size:18px;color:var(--plum-text)}
  .intro-text{left:0;top:430px;width:900px;text-align:center;font-size:9.5px;color:var(--body)}

  /* Content */
  .side{top:488px;width:123px;height:451px;background:var(--side-bg)}
  .block-title{left:137px;font-family:"Oswald",sans-serif;font-weight:300;font-size:12px;color:#111;letter-spacing:.3px}
  .block-text{left:137px;width:140px;font-size:8.6px;line-height:14px;color:var(--body)}
  .more{font-size:8.8px;color:var(--plum-text);display:flex;align-items:center;gap:6px}
  .card{width:147px}
  .card-media{margin-left:6px;width:134px;height:117px}
  .card-caption{text-align:center;font-size:9px;color:#222;margin-top:10px}
  .card-bar{height:3px;background:var(--rule);margin-top:10px}
  .divider{left:137px;top:708px;width:624px;height:1px;background:#e2e2e2}

  /* Footer */
  .site-footer{left:0;top:939px;width:900px;height:219px;background:var(--plum)}
  .foot-title{top:975px;font-family:"Oswald",sans-serif;font-weight:400;font-size:12px;color:#fff;letter-spacing:.4px}
  .foot-list{left:135px;top:1004px;list-style:none;font-size:9px;line-height:19px;color:var(--footer-text)}
  .quote{left:301px;width:125px;font-size:8.4px;line-height:13px;font-style:italic;color:var(--footer-text)}
  .quote b{display:block;font-style:normal;font-weight:600;color:#fff;margin-top:3px}
  .contact{left:467px;top:1005px;font-size:9px;line-height:14px;color:var(--footer-text)}
  .contact-row{display:flex;gap:8px;margin-bottom:6px}
  .contact-row svg{flex:none;margin-top:2px}
  .social{left:467px;top:1085px;display:flex;gap:7px}
  .social span{width:16px;height:16px;border-radius:50%;background:#fff}
  .news-text{left:634px;top:1008px;width:140px;font-size:9px;line-height:14px;color:var(--footer-text)}
  .field{left:634px;width:119px;height:16px;background:var(--field);font-size:8px;color:#8a7c8c;padding-left:4px;line-height:16px}
  .submit{left:635px;top:1092px;width:58px;height:16px;background:#fff;font-size:8.5px;font-weight:600;color:#222;text-align:center;line-height:16px;letter-spacing:.4px}
  .bottom-bar{left:0;top:1158px;width:900px;height:42px;background:var(--plum-dark)}
  .copyright{left:133px;top:1173px;font-size:8.5px;color:var(--footer-text)}
</style>
</head>
<body>

<header class="abs site-header"></header>
<div class="abs brand"><span class="brand-dot"></span>Still Water Healing</div>
<nav class="abs main-nav"><span>HOME</span><span>ABOUT US</span><span>PRODUCTS</span><span>INSTRUCTORS</span><span>BLOG</span><span>CONTACT US</span></nav>

<section class="abs hero" role="img" aria-label="Sunlit forest with rays of light through tall trees and autumn leaves on the ground"></section>
<div class="abs hero-arrow" style="left:28px"><svg width="28" height="28"><path d="M16 9l-5 5 5 5" stroke="#555" stroke-width="2" fill="none"/></svg></div>
<div class="abs hero-arrow" style="left:844px"><svg width="28" height="28"><path d="M12 9l5 5-5 5" stroke="#555" stroke-width="2" fill="none"/></svg></div>
<h1 class="abs hero-title">LOREM IPSUM DOLOR SIT AMET</h1>
<p class="abs hero-text">SED UT PERSPICIATIS UNDE OMNIS ISTE NATUS ERROR SIT VOLUPTATEM ACCUSANTIUM DOLOREMQUE LAUDANTIUM, TOTAM REM APERIAM, EAQUE IPSA QUAE AB ILLO...</p>
<div class="abs hero-btn">READ MORE</div>

<h2 class="abs intro-title">Excepteur Sint Occaecat Cupidatat</h2>
<p class="abs intro-text">Sed ut perspiciatis unde omnis iste natus error sit voluptatem accusantium doloremque laudantium</p>

<div class="abs side" style="left:0"></div>
<div class="abs side" style="left:777px"></div>

<h3 class="abs block-title" style="top:515px">ABOUT STILL WATER HEALING</h3>
<p class="abs block-text" style="top:555px">Lorem ipsum dolor sit amet, consectetur adipiscing elit. Proin sed ipsum tortor. Nam aliquam lacinia elementum. Lorem ipsum dolor sit amet, consectetur adipiscing elit.</p>
<div class="abs more" style="left:225px;top:644px">Learn More <svg width="6" height="8"><path d="M1 1l3 3-3 3" stroke="var(--plum-text)" stroke-width="1.6" fill="none"/></svg></div>

<div class="abs card" style="left:300px;top:517px"><div class="card-media" role="img" aria-label="Hands giving a calming face massage" style="background:linear-gradient(135deg,#f3e3d3,#e8b892)"></div><p class="card-caption">Healing Practices</p><div class="card-bar"></div></div>
<div class="abs card" style="left:453px;top:517px"><div class="card-media" role="img" aria-label="Portrait of a healing instructor in a bright room" style="background:linear-gradient(160deg,#eef0f2,#d8c8b8)"></div><p class="card-caption">Visit Healing Instructors</p><div class="card-bar"></div></div>
<div class="abs card" style="left:606px;top:517px"><div class="card-media" role="img" aria-label="Blossoming trees by a lake at sunset" style="background:linear-gradient(180deg,#e9b27a,#b98ac6 55%,#3a3d5e)"></div><p class="card-caption">Still Water Video</p><div class="card-bar"></div></div>

<div class="abs divider"></div>

<h3 class="abs block-title" style="top:748px">LATEST POSTS</h3>
<p class="abs block-text" style="top:788px">Nam libero tempore, cum soluta nobis est eligendi optio cumque nihil impedit quo minus id quod maxime placeat facere possimus, omnis voluptas assumenda est, omnis dolor repellendus.</p>
<div class="abs more" style="left:234px;top:877px">Visit Blog <svg width="6" height="8"><path d="M1 1l3 3-3 3" stroke="var(--plum-text)" stroke-width="1.6" fill="none"/></svg></div>

<div class="abs card" style="left:300px;top:750px"><div class="card-media" role="img" aria-label="Silhouette meditating in a yoga pose at sunrise" style="background:linear-gradient(180deg,#2a52a8,#7f9ad8 55%,#1b2440)"></div><p class="card-caption">Reducing Stress</p><div class="card-bar"></div></div>
<div class="abs card" style="left:453px;top:750px"><div class="card-media" role="img" aria-label="Desert cliffs reflected in a calm purple lake" style="background:linear-gradient(180deg,#9d7bc4,#8a5a4a 50%,#5c3f7a)"></div><p class="card-caption">Deepening spiritual connection</p><div class="card-bar"></div></div>
<div class="abs card" style="left:606px;top:750px"><div class="card-media" role="img" aria-label="Person stretching joyfully in a green meadow" style="background:linear-gradient(160deg,#5f8c2e,#a4c85a 60%,#4f7a22)"></div><p class="card-caption">Strengthening the Immune</p><div class="card-bar"></div></div>

<footer class="abs site-footer"></footer>
<h4 class="abs foot-title" style="left:135px">Healing Practices</h4>
<ul class="abs foot-list"><li>Acupuncture</li><li>Aromatherapy</li><li>Chiropractic</li><li>Healing Touch</li><li>Massage Therapy</li><li>Breathwork</li></ul>

<h4 class="abs foot-title" style="left:301px">Testimonials</h4>
<p class="abs quote" style="top:1003px">“At vero eos et accusamus et iusto odio dignissimos ducimus” <b>By Clara Dunmore</b></p>
<p class="abs quote" style="top:1071px">“Temporibus autem quibus dam et aut officiis debitis aut rerum” <b>By Elena Varga</b></p>

<h4 class="abs foot-title" style="left:467px">Contact Us</h4>
<div class="abs contact">
  <div class="contact-row"><svg width="10" height="10"><path d="M1 5L5 1l4 4v4H1z" fill="#fff"/></svg><span>Lorem Ipsum Street,<br>Lorem Ipsum</span></div>
  <div class="contact-row"><svg width="10" height="10"><path d="M2 1h2l1 2-1 1c.6 1.3 1.7 2.4 3 3l1-1 2 1v2c-4.5 0-8-3.5-8-8z" fill="#fff"/></svg><span>555-014-2290</span></div>
  <div class="contact-row"><svg width="10" height="8"><rect x="0.5" y="0.5" width="9" height="7" fill="none" stroke="#fff"/><path d="M.5 .5l4.5 4 4.5-4" stroke="#fff" fill="none"/></svg><span>info@stillwaterhealing.com</span></div>
</div>
<div class="abs social"><span></span><span></span><span></span><span></span></div>

<h4 class="abs foot-title" style="left:634px">Newsletter</h4>
<p class="abs news-text">Join Still Water Healing and begin your journey on balanced living.</p>
<div class="abs field" style="top:1046px">Name</div>
<div class="abs field" style="top:1069px">Email</div>
<div class="abs submit">SUBMIT</div>

<div class="abs bottom-bar"></div>
<p class="abs copyright">© Copyright 2013 still water healing. All Rights Reserved</p>

</body>
</html>
```